Simple Landing Page in NFT/Crypto Space for new project

Need a website design built out for a company called "Kestrel Loop". Looking for a very minimalistic website, can use a few graphics but simple and easy, would love to stick primarily to black and white but can have pops of color. This will be a landing page for a new NFT project coming out, I can provide copy for the site. The copy/ideas we have is attached.

```html
<!DOCTYPE html>
<html lang="en">
<head>
<meta charset="utf-8">
<title>Kestrel Loop</title>
<link href="https://fonts.googleapis.com/css2?family=IBM+Plex+Sans:ital,wght@0,400;0,500;0,600;1,600&display=swap" rel="stylesheet">
<style>
  :root {
    --black: #000000;
    --white: #ffffff;
    --pink: #ff2fa8;
    --pink-line: #d42c8c;
    --plum: #5a1238;
    --violet: #2a0a33;
    --card-border: #b0246f;
    --blob-a: #d98ae0;
    --blob-b: #7a3a8a;
  }
  * { box-sizing: border-box; margin: 0; padding: 0; }
  html, body { width: 1200px; height: 3897px; overflow: hidden; background: var(--black); }
  body { position: relative; font-family: "IBM Plex Sans", Arial, sans-serif; color: var(--white); }
  a { color: inherit; text-decoration: none; }

  .site-header { position: absolute; left: 0; top: 0; width: 1200px; height: 144px; background: var(--black); }
  .brand-box { position: absolute; left: 112px; top: 33px; width: 136px; height: 68px; background: var(--pink);
    display: flex; align-items: center; justify-content: center; font-weight: 600; font-size: 19px; color: var(--white); }
  .main-nav { position: absolute; left: 345px; top: 62px; display: flex; gap: 25px; font-size: 16px; font-weight: 500; color: var(--pink); }
  .social { position: absolute; display: flex; gap: 30px; font-size: 15px; font-weight: 600; color: var(--pink); }
  .social-header { left: 765px; top: 62px; }
  .wallet-btn { position: absolute; left: 938px; top: 50px; width: 150px; height: 47px; background: var(--white);
    color: var(--pink); font-size: 14px; display: flex; align-items: center; justify-content: center; }

  .double-rule { position: absolute; left: 0; width: 1200px; height: 6px;
    border-top: 2px solid var(--pink-line); border-bottom: 2px solid var(--pink-line); }

  .hero { position: absolute; left: 0; top: 150px; width: 1200px; height: 693px; background: #07070c; overflow: hidden; }
  .hero-art { position: absolute; right: 0; top: 80px; width: 595px; height: 613px;
    background: radial-gradient(ellipse at 40% 40%, #3a5cff 0%, #2236d8 35%, #19b5d8 60%, #c22bd1 80%, transparent 95%); }
  .hero-quote { position: absolute; left: 112px; top: 200px; width: 500px; font-size: 42px; line-height: 51px; font-weight: 400; }
  .hero-cite { position: absolute; left: 112px; top: 378px; font-size: 22px; font-style: italic; font-weight: 600; }
  .btn-outline { position: absolute; width: 204px; height: 70px; border: 3px solid var(--pink); border-radius: 6px;
    background: var(--plum); color: var(--white); font-size: 20px; font-weight: 500;
    display: flex; align-items: center; justify-content: center; }
  .hero .btn-outline { left: 112px; top: 443px; }

  .about { position: absolute; left: 0; top: 843px; width: 1200px; height: 546px; text-align: center; }
  .about h2 { position: absolute; left: 0; top: 88px; width: 1200px; font-size: 40px; font-weight: 500; }
  .about p { position: absolute; left: 200px; top: 171px; width: 800px; font-size: 20px; line-height: 31px; }
  .about .btn-outline { left: 508px; top: 381px; }

  .roadmap { position: absolute; left: 0; top: 1395px; width: 1200px; height: 2330px;
    background: linear-gradient(180deg, #000 0%, #1a0620 12%, var(--violet) 60%, #200828 100%); }
  .roadmap h2 { position: absolute; left: 112px; top: 88px; font-size: 40px; font-weight: 500; }
  .timeline-line { position: absolute; left: 156px; top: 309px; width: 3px; height: 1811px; background: var(--pink); }
  .timeline-dot { position: absolute; left: 145px; width: 25px; height: 25px; border-radius: 50%;
    background: var(--white); border: 3px solid var(--pink); }
  .milestone { position: absolute; left: 234px; width: 746px; height: 176px; background: var(--black);
    border: 1px solid var(--card-border); }
  .milestone h3 { position: absolute; font-size: 20px; font-weight: 500; }
  .milestone p { position: absolute; font-size: 14.5px; line-height: 26px; width: 560px; }
  .milestone.art-right h3, .milestone.art-right p { left: 40px; }
  .milestone.art-right h3 { top: 36px; color: var(--pink); }
  .milestone.art-right p { top: 78px; }
  .milestone.art-left h3, .milestone.art-left p { left: 133px; }
  .milestone.art-left h3 { top: 50px; }
  .milestone.art-left p { top: 92px; }
  .milestone.final p { left: 100px; top: 58px; width: 546px; text-align: center; color: var(--pink); }
  .numeral-art { position: absolute; width: 98px; height: 130px; border-radius: 40% 40% 30% 30%;
    background: linear-gradient(160deg, var(--blob-a), var(--blob-b)); }
  .art-right .numeral-art { left: 666px; top: -14px; }
  .art-left .numeral-art { left: 24px; top: -12px; }

  .site-footer { position: absolute; left: 0; top: 3725px; width: 1200px; height: 172px; background: var(--pink); }
  .footer-brand { position: absolute; left: 159px; top: 72px; font-size: 24px; font-weight: 600; color: var(--white); }
  .footer-nav { position: absolute; left: 418px; top: 81px; display: flex; gap: 24px; font-size: 17px; font-weight: 500; color: var(--black); }
  .social-footer { left: 960px; top: 80px; color: var(--black); }
</style>
</head>
<body>
  <header class="site-header">
    <div class="brand-box">Kestrel Loop</div>
    <nav class="main-nav"><a href="#">HOME</a><a href="#">ABOUT</a><a href="#">ROADMAP</a><a href="#">CONTACT US</a></nav>
    <div class="social social-header"><span>Chirper</span><span>Huddle</span></div>
    <a class="wallet-btn" href="#">CONNECT WALLET</a>
  </header>
  <div class="double-rule" style="top:144px"></div>

  <section class="hero">
    <div class="hero-art" role="img" aria-label="Blue and pink wireframe sculpture of a crouching figure"></div>
    <p class="hero-quote">Go down deep enough into anything and you will find mathematics.</p>
    <p class="hero-cite">— Marek Holloway</p>
    <a class="btn-outline" href="#">Learn More</a>
  </section>

  <section class="about">
    <h2>ABOUT US</h2>
    <p>Kestrel Loop is a collection of 1327 randomly generated Math Based NFT's on the Aethernet blockchain. We are the FIRST pure math based NFT with a solid roadmap to provide continual value to our holders. Our Alpha-based community revolves entirely around using data and logic, the backbone of mathematics, to make informed decisions in the crazy world of NFT's and Crypto.</p>
    <a class="btn-outline" href="#">Read More</a>
  </section>
  <div class="double-rule" style="top:1389px"></div>

  <section class="roadmap">
    <h2>ROAD MAP</h2>
    <div class="timeline-line"></div>
    <span class="timeline-dot" style="top:296px"></span>
    <span class="timeline-dot" style="top:511px"></span>
    <span class="timeline-dot" style="top:737px"></span>
    <span class="timeline-dot" style="top:964px"></span>
    <span class="timeline-dot" style="top:1193px"></span>
    <span class="timeline-dot" style="top:1421px"></span>
    <span class="timeline-dot" style="top:1650px"></span>
    <span class="timeline-dot" style="top:1877px"></span>
    <span class="timeline-dot" style="top:2107px"></span>

    <article class="milestone art-right" style="top:221px">
      <div class="numeral-art" role="img" aria-label="Glossy purple 3D numeral two"></div>
      <h3>0% - A pre-sale reverse dutch auction will take place.</h3>
      <p>The price of each Genesis + NFT will start a 2AETH and go down as the auction progresses. When they are sold out, they are sold out! Watch our Huddle for updates.</p>
    </article>
    <article class="milestone art-left" style="top:433px">
      <div class="numeral-art" role="img" aria-label="Glossy purple 3D numeral two"></div>
      <h3>13% - Opening of the Genesis Community</h3>
      <p>By pricing our mint the way we are, we are aiming to create the best place on the internet to hang out and receive ALPHA on all things NFT and Crypto.</p>
    </article>
    <article class="milestone art-right" style="top:663px">
      <div class="numeral-art" role="img" aria-label="Glossy purple 3D numeral two"></div>
      <h3>29% -&nbsp; Subtraction launch</h3>
      <p>Our next generation of NFT's will launch, expanding our community. In order to mint, you will need to hold a Genesis + NFT and burn xxx amount of $QUILL.</p>
    </article>
    <article class="milestone art-left" style="top:890px">
      <div class="numeral-art" role="img" aria-label="Glossy purple 3D numeral two"></div>
      <h3>44% - Multiplication launch</h3>
      <p>The third collection will launch. In order to mint, you will need to hold both a Genesis + and a Subtraction NFT - as well as burn xxx amount of $QUILL.</p>
    </article>
    <article class="milestone art-right" style="top:1120px">
      <div class="numeral-art" role="img" aria-label="Glossy purple 3D numeral two"></div>
      <h3>57% - Division Launch</h3>
      <p>The fourth collection will launch. In order to mint, you will need to hold both a Subtraction and a Multiplication NFT - as well as burn xxx amount of $QUILL.</p>
    </article>
    <article class="milestone art-left" style="top:1348px">
      <div class="numeral-art" role="img" aria-label="Glossy purple 3D numeral two"></div>
      <h3>69% - Squared Launch</h3>
      <p>The fifth collection will launch. In order to mint, you will need to hold both a Multiplication and Division NFT - as well as burn xxx amount of $QUILL.</p>
    </article>
    <article class="milestone art-right" style="top:1575px">
      <div class="numeral-art" role="img" aria-label="Glossy purple 3D numeral two"></div>
      <h3>81% - Square Root Launch</h3>
      <p>The sixth collection will launch. In order to mint, you will need to hold both a Division and Squared NFT - as well as burn xxx amount of $QUILL.</p>
    </article>
    <article class="milestone art-left" style="top:1802px">
      <div class="numeral-art" role="img" aria-label="Glossy purple 3D numeral two"></div>
      <h3>95% - Cubed Launch</h3>
      <p>The seventh collection will launch. In order to mint, you will need to hold both a Squared and a Square Root NFT - as well as burn xxx amount of $QUILL.</p>
    </article>
    <article class="milestone final" style="top:2032px">
      <p>100% - Roadmap 2.0 comes out with ability to mint and produce art and graphical pieces based on what collection(s) and mathematical functions you own</p>
    </article>
  </section>

  <footer class="site-footer">
    <div class="footer-brand">Kestrel Loop</div>
    <nav class="footer-nav"><a href="#">HOME</a><a href="#">ABOUT</a><a href="#">ROADMAP</a><a href="#">CONTACT US</a></nav>
    <div class="social social-footer"><span>Chirper</span><span>Huddle</span></div>
  </footer>
</body>
</html>
```